TC Fruit Trays / Fruit Basket sign

We are Tansy Corner, a supermarket franchisee. We need a more professional look on some of our in-store signs. I will attach a jpg of an existing sign, and also share a dropbox folder with our current logos.
https://www.filebarn.net/sh/k4pq8zt1mmwe2xr/Qa7T3Hn9Km
Here is a link to our Mr. Bolt character art, but use it sparingly - it looks bad to have too much of it in our graphics:
https://www.filebarn.net/sh/v8cn2jd5ttqu4ly/Rf3KsLe8Xo
In fact, you may choose not to use the character art work, if you feel the design looks more professional. This is the first project we have tried using SketchHive, and have many more sign projects that also need to be done. The winning design choice will get first shot at the remaining design projects. Thanks!
Adults 18+
Store

```html
<!DOCTYPE html>
<html lang="en">
<head>
<meta charset="UTF-8">
<title>Tansy Corner – Fruit Trays or Fruit Baskets</title>
<link rel="stylesheet" href="https://fonts.googleapis.com/css2?family=Francois+One&display=swap">
<style>
  :root {
    --brand-blue: #1ba3e0;
    --headline-blue: #1a9fdc;
    --sky-white: #ffffff;
    --glow-center: #fbfdf3;
    --glow-edge: #d9eaa6;
    --photo-warm: #e7c98f;
    --photo-light: #efe3c4;
  }
  * { margin: 0; padding: 0; box-sizing: border-box; }
  html, body {
    width: 1200px;
    height: 452px;
    overflow: hidden;
    background: var(--sky-white);
  }
  .sign {
    position: relative;
    width: 1200px;
    height: 452px;
    overflow: hidden;
    font-family: "Francois One", "Arial Narrow", sans-serif;
  }
  .sign__hero {
    position: absolute;
    inset: 0 0 136px 0;
    background: radial-gradient(ellipse 720px 420px at 560px 210px, var(--glow-center) 0%, #f0f6d6 45%, var(--glow-edge) 100%);
  }
  .sign__headline {
    position: absolute;
    left: 78px;
    top: 48px;
    color: var(--headline-blue);
    font-size: 114px;
    line-height: 96px;
    letter-spacing: 0;
    text-transform: uppercase;
    font-weight: 400;
    white-space: nowrap;
    transform: scaleX(0.93);
    transform-origin: left top;
  }
  .sign__photo {
    position: absolute;
    left: 800px;
    top: 14px;
    width: 355px;
    height: 302px;
    border-radius: 24px 24px 12px 12px;
    background: linear-gradient(160deg, var(--photo-light) 0%, var(--photo-warm) 100%);
  }
  .sign__divider {
    position: absolute;
    left: 0;
    top: 316px;
    width: 1200px;
    height: 6px;
    background: var(--sky-white);
  }
  .sign__band {
    position: absolute;
    left: 0;
    top: 322px;
    width: 1200px;
    height: 130px;
    background: var(--brand-blue);
  }
  .brand {
    position: absolute;
    left: 24px;
    top: 32px;
    display: flex;
    align-items: center;
    gap: 12px;
    color: var(--sky-white);
  }
  .brand__dot {
    width: 58px;
    height: 58px;
    border-radius: 50%;
    background: var(--sky-white);
  }
  .brand__name {
    font-size: 30px;
    line-height: 1;
  }
  .band__message {
    position: absolute;
    left: 318px;
    top: 18px;
    color: var(--sky-white);
    font-size: 72px;
    line-height: 84px;
    letter-spacing: 3px;
    white-space: nowrap;
  }
  .band__note {
    position: absolute;
    left: 1022px;
    top: 60px;
    color: var(--sky-white);
    font-size: 29px;
    line-height: 34px;
    white-space: nowrap;
  }
</style>
</head>
<body>
  <main class="sign">
    <section class="sign__hero">
      <h1 class="sign__headline">Fruit Trays or<br>Fruit Baskets</h1>
      <div class="sign__photo" role="img" aria-label="Photo of a wicker basket filled with grapes, apples, oranges, a pear and bananas"></div>
    </section>
    <div class="sign__divider"></div>
    <footer class="sign__band">
      <div class="brand">
        <span class="brand__dot"></span>
        <span class="brand__name">Tansy Corner</span>
      </div>
      <p class="band__message">We Make On Request</p>
      <p class="band__note">Prices Vary.</p>
    </footer>
  </main>
</body>
</html>
```